Website for company called VORENTbio

We need a website for our new company called VORENTbio which developed a platform/technology to identify antigen-specific T cells (immune cells) which can be used for cancer therapy, autoimmunity, etc.

The platform is called VORENT and is rapid, versatile, unbiased, and inexpensive.

We have a semi-final logo although we are not completely set on color and font of text (attached).

Target Market(s)

Our target audience at the moment would be potential investors and VCs. We eventually are interested in getting attention from scientists and cell/immunotherapy companies.

Industry/Entity Type

Healthcare/Technology

Coding

Coded - Design and coding required

Number of Pages Required

1 page

Colors
0094D4
00A9DD
6FCCEA
C7EBF8
E9F6FB
00AB8E
00BBA5
67D7C9
C6EFE9
E9F9F6
E54698
E96AAD
F1A4CE
F9D9EA
FCEFF6
A7469A
B969AE
D3A5CF
EDDBEB
F8F0F9
6B429C
8869AF
B7A5CE
E3DAEB
F3F0F8

Requirements
Must have
• Landing page about the company, About us page, Technology page (could be merged with company landing page), Contact us page

```html
<!DOCTYPE html>
<html lang="en">
<head>
<meta charset="utf-8">
<title>VORENTbio</title>
<link href="https://fonts.googleapis.com/css2?family=Montserrat:wght@400;500;600;700;800&display=swap" rel="stylesheet">
<style>
:root{
  --blue:#2a7fd4;
  --blue-light:#3d9be0;
  --purple:#6b44b2;
  --purple-deep:#6a3fa6;
  --ink:#111;
  --text:#444;
  --panel:#f3f3f3;
  --white:#fff;
  --grad:linear-gradient(90deg,#2a7fd4,#6b44b2);
}
*{margin:0;padding:0;box-sizing:border-box}
html,body{width:1200px;height:4559px;overflow:hidden}
body{font-family:'Montserrat',sans-serif;color:var(--ink);background:var(--white);position:relative}
.abs{position:absolute}
.btn{position:absolute;display:flex;align-items:center;justify-content:center;background:var(--grad);color:var(--white);font-weight:700;font-size:13px;border-radius:24px;text-transform:uppercase;box-shadow:0 4px 10px rgba(60,70,180,.25)}
.topline{top:0;left:50px;width:1100px;height:5px;background:var(--grad)}
.brand{font-weight:700;color:var(--blue);display:flex;align-items:center;gap:10px}
.brand .dot{width:22px;height:22px;border-radius:50%;background:currentColor}
.header .brand{left:127px;top:33px;font-size:36px}
.nav{top:44px;display:flex;font-size:15px;font-weight:500;color:#333}
.nav a{position:absolute;white-space:nowrap}
.nav .active:after{content:"";position:absolute;left:0;right:0;bottom:-8px;height:2px;background:#333}
.header .divider{left:919px;top:38px;width:2px;height:34px;background:var(--purple)}
.header .phone{left:945px;top:42px;font-size:19px;font-weight:700;color:var(--purple-deep)}
.hero{top:99px;left:0;width:1200px;height:579px;background:linear-gradient(90deg,#58a7dc 0%,#7da6df 40%,#9a8fd4 65%,#a88bd0 100%)}
.hero-title{left:704px;top:290px;font-size:56px;font-weight:700;color:var(--white)}
.hero-sub{left:704px;top:360px;width:380px;font-size:21px;line-height:26px;font-weight:500;color:var(--white)}
.hero .btn,.hero-btn{left:704px;top:434px;width:141px;height:42px;border:2px solid var(--white)}
.services{top:627px;left:103px;width:994px;height:492px;background:var(--panel);border-radius:12px}
.svc{position:absolute;top:54px;width:267px}
.svc .photo{width:267px;height:186px;border-radius:8px;box-shadow:0 8px 14px rgba(0,0,0,.15)}
.svc h3{margin-top:26px;font-size:19px;font-weight:700}
.svc p{margin-top:12px;font-size:14px;line-height:21px;color:var(--text)}
.svc .btn{position:relative;margin-top:20px;width:142px;height:44px}
.about-art{left:191px;top:1197px;width:361px;height:463px;border-radius:50%;background:radial-gradient(circle,#7a4bd0 0%,#3a5fcf 50%,#1c3a8f 100%)}
.about-title{left:628px;top:1262px;font-size:36px;font-weight:800}
.about-text{left:628px;top:1325px;width:426px;font-size:14.5px;line-height:22.2px;color:#333}
.about-btn{left:628px;top:1573px;width:156px;height:45px;font-size:14px}
.features{top:1715px;left:0;width:1200px;height:409px;background:var(--purple)}
.feat{position:absolute;top:70px;width:240px;text-align:center;color:var(--white)}
.feat svg{display:block;margin:0 auto}
.feat h3{margin-top:34px;font-size:30px;font-weight:700}
.feat p{margin-top:14px;font-size:14px;line-height:21px}
.sec-title{width:1200px;text-align:center;font-size:36px;font-weight:800}
.event{position:absolute;top:2306px;width:292px;height:365px;background:var(--white);box-shadow:0 4px 16px rgba(0,0,0,.08)}
.event .photo{margin:14px 14px 0;width:264px;height:199px;border-radius:8px}
.event .date{margin:22px 0 0 18px;font-size:12px;font-weight:700;color:var(--purple)}
.event h4{margin:6px 18px 0;font-size:19px;line-height:22px;font-weight:700}
.event p{margin:12px 18px 0;font-size:13.5px;line-height:18px;color:var(--text)}
.resources{top:2772px;left:0;width:1200px;height:793px;background:var(--panel)}
.res{position:absolute;width:441px;height:216px;background:var(--white);box-shadow:0 4px 14px rgba(0,0,0,.06)}
.res h4{position:absolute;left:39px;top:44px;width:340px;font-size:20px;line-height:24px;font-weight:700}
.res p{position:absolute;left:39px;top:108px;width:340px;font-size:14px;line-height:23px;color:var(--text)}
.res .arrow{position:absolute;right:-23px;top:85px;width:46px;height:46px;border-radius:50%;background:var(--grad)}
.prog-title{left:127px;top:3612px;width:420px;font-size:27.5px;line-height:33px;font-weight:800}
.prog-text{left:127px;top:3795px;width:420px;font-size:14.5px;line-height:25.5px;color:#333}
.prog-photo{left:570px;top:3482px;width:503px;height:493px;background:linear-gradient(135deg,#b9c6cc,#d8d2c6 50%,#6d8fa8)}
.footer{top:4105px;left:0;width:1200px;height:454px;background:linear-gradient(90deg,#3b7fd6,#5a60c0 60%,#6a44ac)}
.footer .brand{left:133px;top:78px;font-size:46px;color:var(--white)}
.footer .call{left:731px;top:92px;font-size:27px;font-weight:700;color:var(--white);display:flex;align-items:center;gap:18px}
.footer .rule{left:129px;top:196px;width:944px;height:1px;background:rgba(255,255,255,.3)}
.social{left:129px;top:230px;display:flex;gap:22px}
.social span{width:14px;height:14px;border-radius:50%;background:var(--white)}
.fnav{top:233px;font-size:13px;font-weight:600;color:var(--white)}
.fnav a,.nav a{text-decoration:none;color:inherit}
.copy{left:854px;top:278px;font-size:13px;color:var(--white)}
.fband{left:0;top:364px;width:1200px;height:90px;background:rgba(80,60,170,.25)}
</style>
</head>
<body>
<div class="abs topline"></div>
<header class="header">
  <div class="abs brand"><span class="dot"></span>vorentbio</div>
  <nav class="abs nav">
    <a class="active" style="left:428px">HOME</a>
    <a style="left:517px">ABOUT US</a>
    <a style="left:639px">TECHNOLOGY</a>
    <a style="left:789px">CONTACT US</a>
  </nav>
  <div class="abs divider"></div>
  <div class="abs phone">555 014 2290</div>
</header>

<section class="abs hero" role="img" aria-label="Photo of a doctor with a tablet talking to a patient in a hospital bed, fading into purple"></section>
<h1 class="abs hero-title">VORENTbio</h1>
<p class="abs hero-sub">Lorem ipsum dolor sit ametconsec tetur adipiscing elit sed do.</p>
<a class="btn hero-btn">Contact us</a>

<section class="abs services">
  <div class="svc" style="left:67px">
    <div class="photo" role="img" aria-label="Microscopic image of a blue cell" style="background:linear-gradient(135deg,#7fb4e8,#1f5fbf 55%,#c8d9f2)"></div>
    <h3>CANCER THERAPY</h3>
    <p>Lorem ipsum dolor sit amet, consectetur adipiscing elit, sed do eiusmod tempor incidi.</p>
    <a class="btn">Read more</a>
  </div>
  <div class="svc" style="left:363px">
    <div class="photo" role="img" aria-label="Gloved hand at a throat" style="background:linear-gradient(135deg,#f1d6cf,#e8e6ec 55%,#e79ab5)"></div>
    <h3>AUTOIMMUNITY</h3>
    <p>Lorem ipsum dolor sit amet, consectetur adipiscing elit, sed do eiusmod tempor incidi.</p>
    <a class="btn">Read more</a>
  </div>
  <div class="svc" style="left:658px">
    <div class="photo" role="img" aria-label="Doctor writing notes during a consultation" style="background:linear-gradient(135deg,#c9ced3,#8b6f62 55%,#3f3a3a)"></div>
    <h3>OTHER SERVICES</h3>
    <p>Lorem ipsum dolor sit amet, consectetur adipiscing elit, sed do eiusmod tempor incidi.</p>
    <a class="btn">Read more</a>
  </div>
</section>

<div class="abs about-art" role="img" aria-label="Molecular cell imagery in blue and violet"></div>
<h2 class="abs about-title">ABOUT VORENTBIO</h2>
<p class="abs about-text">Lorem ipsum dolor sit amet, consectetur adip is cing elit, sed do eiusmod tempor incididunt lorut labo re et dolore magna aliqua. Quis ipsum sus pendisse ultrices gravida. Risus commodo vive rra maecenas accumsan lacel facilisiorem ipsu m dolor sit amet, consectetur adip is cing elit, sed do eiusmod tempor incididunt lorut labo re et dolore magna aliqua. Quis ipsum sus pend isse ultrices gravida. Risus commodo vive rra mae cenas accumsan lacdo eiusmod tempor incididunt lorut labo re et dolor.</p>
<a class="btn about-btn">Read more</a>

<section class="abs features">
  <div class="feat" style="left:110px">
    <svg width="90" height="84" viewBox="0 0 90 84"><circle cx="40" cy="44" r="36" fill="none" stroke="#fff" stroke-width="2.5" stroke-dasharray="1 7" stroke-linecap="round"/><path d="M24 42 L40 62 L84 6 L40 46 Z" fill="#fff"/></svg>
    <h3>RAPID</h3><p>Lorem ipsum dolor sit<br>amet consectetur</p>
  </div>
  <div class="feat" style="left:317px">
    <svg width="90" height="84" viewBox="0 0 90 84"><circle cx="40" cy="44" r="36" fill="none" stroke="#fff" stroke-width="2.5" stroke-dasharray="1 7" stroke-linecap="round"/><path d="M24 42 L40 62 L84 6 L40 46 Z" fill="#fff"/></svg>
    <h3>VERSATILE</h3><p>Lorem ipsum dolor sit<br>amet consectetur</p>
  </div>
  <div class="feat" style="left:554px">
    <svg width="90" height="84" viewBox="0 0 90 84"><circle cx="40" cy="44" r="36" fill="none" stroke="#fff" stroke-width="2.5" stroke-dasharray="1 7" stroke-linecap="round"/><path d="M24 42 L40 62 L84 6 L40 46 Z" fill="#fff"/></svg>
    <h3>UNBIASED</h3><p>Lorem ipsum dolor sit<br>amet consectetur</p>
  </div>
  <div class="feat" style="left:813px">
    <svg width="90" height="84" viewBox="0 0 90 84"><circle cx="40" cy="44" r="36" fill="none" stroke="#fff" stroke-width="2.5" stroke-dasharray="1 7" stroke-linecap="round"/><path d="M24 42 L40 62 L84 6 L40 46 Z" fill="#fff"/></svg>
    <h3>INEXPENSIVE</h3><p>Lorem ipsum dolor sit<br>amet consectetur</p>
  </div>
</section>

<svg class="abs" style="left:575px;top:2189px" width="50" height="22" viewBox="0 0 50 22"><circle cx="11" cy="11" r="10" fill="#2a7fd4"/><circle cx="39" cy="11" r="10" fill="#6b44b2"/><rect x="11" y="7" width="28" height="8" fill="#4a62c4"/></svg>
<h2 class="abs sec-title" style="top:2222px">UPCOMING EVENTS</h2>
<article class="event" style="left:127px">
  <div class="photo" role="img" aria-label="Blue molecular strand close-up" style="background:linear-gradient(135deg,#9cc7ec,#3c7fc9 50%,#cfe1f3)"></div>
  <div class="date">18 JULY 25</div><h4>Lorem ipsum dolor sit amet consectetur</h4><p>Lorem ipsum dolor sit aloreme cons ectetur adipiscing</p>
</article>
<article class="event" style="left:455px">
  <div class="photo" role="img" aria-label="Woman in a headscarf outdoors holding a mug" style="background:linear-gradient(135deg,#8b8e6e,#c9b08a 50%,#6e6a58)"></div>
  <div class="date">18 JULY 25</div><h4>Lorem ipsum dolor sit amet consectetur</h4><p>Lorem ipsum dolor sit aloreme cons ectetur adipiscing</p>
</article>
<article class="event" style="left:782px">
  <div class="photo" role="img" aria-label="Microscopic image of a blue cell" style="background:linear-gradient(135deg,#7fb4e8,#1f5fbf 55%,#c8d9f2)"></div>
  <div class="date">18 JULY 25</div><h4>Lorem ipsum dolor sit amet consectetur</h4><p>Lorem ipsum dolor sit aloreme cons ectetur adipiscing</p>
</article>

<section class="abs resources">
  <h2 class="abs sec-title" style="top:73px">RESOURCES</h2>
  <div class="res" style="left:127px;top:159px"><h4>Lorem ipsum dolor sit ametcons ectetur adipiscing elit.</h4><p>Lorem ipsum dolor sit amet, consectetur ad piscing elit, sed do eiusmod tempor loreinc ididunt ut labore.</p><span class="arrow"><svg width="46" height="46" viewBox="0 0 46 46"><path d="M20 15 L28 23 L20 31" fill="none" stroke="#fff" stroke-width="2"/></svg></span></div>
  <div class="res" style="left:632px;top:159px"><h4>Lorem ipsum dolor sit ametcons ectetur adipiscing elit.</h4><p>Lorem ipsum dolor sit amet, consectetur ad piscing elit, sed do eiusmod tempor loreinc ididunt ut labore.</p><span class="arrow"><svg width="46" height="46" viewBox="0 0 46 46"><path d="M20 15 L28 23 L20 31" fill="none" stroke="#fff" stroke-width="2"/></svg></span></div>
  <div class="res" style="left:127px;top:407px"><h4>Lorem ipsum dolor sit ametcons ectetur adipiscing elit.</h4><p>Lorem ipsum dolor sit amet, consectetur ad piscing elit, sed do eiusmod tempor loreinc ididunt ut labore.</p><span class="arrow"><svg width="46" height="46" viewBox="0 0 46 46"><path d="M20 15 L28 23 L20 31" fill="none" stroke="#fff" stroke-width="2"/></svg></span></div>
  <div class="res" style="left:632px;top:407px"><h4>Lorem ipsum dolor sit ametcons ectetur adipiscing elit.</h4><p>Lorem ipsum dolor sit amet, consectetur ad piscing elit, sed do eiusmod tempor loreinc ididunt ut labore.</p><span class="arrow"><svg width="46" height="46" viewBox="0 0 46 46"><path d="M20 15 L28 23 L20 31" fill="none" stroke="#fff" stroke-width="2"/></svg></span></div>
</section>

<div class="abs prog-photo" role="img" aria-label="Nurse in scrubs talking with an older patient"></div>
<h2 class="abs prog-title">WHAT IS THE PROGNOSIS OF USING CAR T-CELL THERAPY FOR PATIENTS WITH LYMPHOMA OR OTHER BLOOD CANCERS?</h2>
<p class="abs prog-text">Lorem ipsum dolor sit amet, consectetur adipiscing elit, sed do eiusmod tempor incididunt ut labore et dolore magna aliqua. Quis ipsum suspendisse ultrices gravida. Risus commodo viverra maecenas accumsan lacus vel facilisis.</p>

<footer class="abs footer">
  <div class="abs fband"></div>
  <div class="abs brand"><span class="dot"></span>vorentbio</div>
  <div class="abs call"><svg width="44" height="44" viewBox="0 0 24 24"><path d="M6.6 10.8a15 15 0 0 0 6.6 6.6l2.2-2.2c.3-.3.7-.4 1-.2 1.1.4 2.3.6 3.6.6.6 0 1 .4 1 1V20c0 .6-.4 1-1 1A17 17 0 0 1 3 4c0-.6.4-1 1-1h3.5c.6 0 1 .4 1 1 0 1.3.2 2.5.6 3.6.1.3 0 .7-.2 1z" fill="none" stroke="#fff" stroke-width="1.2"/></svg>CALL: 555 014 7731</div>
  <div class="abs rule"></div>
  <div class="abs social"><span></span><span></span><span></span><span></span><span></span></div>
  <nav class="abs fnav" style="left:0">
    <a class="abs" style="left:657px">HOME</a>
    <a class="abs" style="left:736px">ABOUT US</a>
    <a class="abs" style="left:845px">TECHNOLOGY</a>
    <a class="abs" style="left:980px;white-space:nowrap">CONTACT US</a>
  </nav>
  <div class="abs copy">2025 © All Rights are Reserved.</div>
</footer>
</body>
</html>
```